BLAC inc Business Card Design

I have a rough draft of the BLAC inc logo that I would like to use on the business card. I also attached our logo for Quillbrook.com. I also included a sample of a business card from another mortgage company that I like. We would like a tagline on the back to say "let's get started" and below Quillbrook.com
Contact Information for Business Card
Brightway Lending and Capital, inc
Marcus Delane
Mortgage Specialist
Direct (555)204-1187
Cell (555)318-4592
Fax (555)907-2263
marcus@quillbrook.com
California Division of Parcel Registry 07493128
FLRB 460315

```html
<!DOCTYPE html>
<html lang="en">
<head>
<meta charset="utf-8">
<title>BLAC inc Business Card</title>
<link rel="stylesheet" href="https://fonts.googleapis.com/css2?family=Open+Sans:wght@400;600;700&family=Kalam:wght@400&display=swap">
<style>
  :root {
    --backdrop: #d8d8d8;
    --navy: #16213f;
    --navy-deep: #111a33;
    --green: #7c9c32;
    --grey-mark: #a9a9be;
    --white: #ffffff;
    --ink-light: #f1f3f7;
  }
  * { box-sizing: border-box; margin: 0; padding: 0; }
  html, body { width: 1200px; height: 900px; overflow: hidden; }
  body {
    background: var(--backdrop);
    font-family: "Open Sans", Arial, sans-serif;
    position: relative;
  }
  .card {
    position: absolute;
    top: 296px;
    width: 540px;
    height: 309px;
    border-radius: 22px;
    overflow: hidden;
    box-shadow: 0 14px 28px rgba(0,0,0,0.18);
  }
  .card--front { left: 40px; background: var(--navy); }
  .card--back {
    left: 620px;
    background: radial-gradient(ellipse at 75% 30%, #1e2b50 0%, var(--navy) 55%, var(--navy-deep) 100%);
  }

  /* front */
  .front__top {
    position: absolute; left: 0; top: 0; width: 100%; height: 146px;
    background: var(--white);
  }
  .front__band {
    position: absolute; left: 0; top: 146px; width: 100%; height: 12px;
    background: var(--green);
  }
  .brand {
    position: absolute; left: 26px; top: 48px;
    display: flex; align-items: center; gap: 12px;
  }
  .brand__dot {
    width: 44px; height: 44px; border-radius: 50%;
    background: var(--grey-mark);
  }
  .brand__name {
    font-size: 27px; font-weight: 700; color: var(--navy); letter-spacing: 0.2px;
  }
  .brand__line {
    position: absolute; left: 28px; top: 104px;
    font-size: 12px; font-weight: 600; color: var(--green);
  }
  .person {
    position: absolute; right: 30px; top: 28px; text-align: right;
  }
  .person__name { font-size: 21px; font-weight: 600; color: var(--green); }
  .person__title { font-size: 13px; color: var(--navy); margin-top: 4px; }

  .contacts {
    position: absolute; left: 24px; top: 174px;
    list-style: none; color: var(--white); font-size: 12.5px; line-height: 20px;
  }
  .contacts li { display: flex; align-items: flex-start; gap: 6px; }
  .contacts svg { width: 12px; height: 12px; margin-top: 4px; flex: none; fill: var(--green); }
  .contacts .indent { padding-left: 18px; }

  /* back */
  .back__tagline {
    position: absolute; left: 0; top: 112px; width: 100%;
    text-align: center; padding-left: 120px;
    font-family: "Kalam", cursive;
    font-size: 26px; color: var(--green);
  }
  .back__site {
    position: absolute; left: 0; bottom: 44px; width: 100%;
    text-align: center; padding-left: 70px;
    font-size: 16px; letter-spacing: 4px; color: var(--ink-light);
  }
</style>
</head>
<body>

<section class="card card--front" aria-label="Business card front">
  <div class="front__top"></div>
  <div class="front__band"></div>

  <div class="brand">
    <span class="brand__dot"></span>
    <span class="brand__name">BLAC inc</span>
  </div>
  <p class="brand__line">Brightway Lending and Capital.com</p>

  <div class="person">
    <p class="person__name">Marcus Delane</p>
    <p class="person__title">Mortgage Specialist</p>
  </div>

  <ul class="contacts">
    <li>
      <svg viewBox="0 0 24 24" aria-hidden="true"><path d="M6.6 10.8a15.1 15.1 0 0 0 6.6 6.6l2.2-2.2c.3-.3.7-.4 1-.2 1.1.4 2.3.6 3.6.6.6 0 1 .4 1 1V20c0 .6-.4 1-1 1A17 17 0 0 1 3 4c0-.6.4-1 1-1h3.5c.6 0 1 .4 1 1 0 1.3.2 2.5.6 3.6.1.3 0 .7-.2 1z"/></svg>
      <span>(555)204-1187</span>
    </li>
    <li>
      <svg viewBox="0 0 24 24" aria-hidden="true"><path d="M7 1h10a2 2 0 0 1 2 2v18a2 2 0 0 1-2 2H7a2 2 0 0 1-2-2V3a2 2 0 0 1 2-2zm0 3v14h10V4z"/></svg>
      <span>(555)318-4592</span>
    </li>
    <li>
      <svg viewBox="0 0 24 24" aria-hidden="true"><path d="M6 2h9l3 3v5h1a3 3 0 0 1 3 3v7a2 2 0 0 1-2 2H4a2 2 0 0 1-2-2v-7a3 3 0 0 1 3-3h1zm2 2v6h8V6h-2V4zm-1 10v2h10v-2z"/></svg>
      <span>(555)907-2263</span>
    </li>
    <li>
      <svg viewBox="0 0 24 24" aria-hidden="true"><path d="M2 5h20v14H2zm2 2v.5l8 5.5 8-5.5V7z"/></svg>
      <span>marcus@quillbrook.com</span>
    </li>
    <li>
      <svg viewBox="0 0 24 24" aria-hidden="true"><path d="M12 2 1 12h3v9h6v-6h4v6h6v-9h3z"/></svg>
      <span>California Division of Parcel Registry</span>
    </li>
    <li class="indent"><span>07493128 FLRB 460315</span></li>
  </ul>
</section>

<section class="card card--back" aria-label="Business card back">
  <p class="back__tagline">let's get started</p>
  <p class="back__site">Quillbrook.com</p>
</section>

</body>
</html>
```